Webdesign for Non profit Diabetes education company

We are looking for a website design for our company.

We just created the company Glucose Guidance Circle

The concept for the company is to educate diabetics with resources that will help them manage their Diabetes. The list of advisers will be dietitians, podiatrist, diabetic educators, and fitness centers.

Please see attached logo. I like the logo to include an image that connects people together.

I've attached our logo, please use the colors in the design of the site.

Creativity is encouraged. Have fun with this project. We are looking for a professional site but not to corporate.

The page must be written in HTML 5 and be responsive built for mobile. You can use bootstrap, jquery, or angular JS.

Wordpress or wix will not be accepted.

The website will be hosted at www.glucoseguidancecircle.example

Requirements
Must have
• The page must be written in HTML 5 and be responsive built for mobile. You can use bootstrap, jquery, or angular JS.
• The landing page should include a splash page. Please incorporate the logo and the
Should not have
• Wordpress or wix will not be accepted.

```html
<!DOCTYPE html>
<html lang="en">
<head>
<meta charset="utf-8">
<title>Glucose Guidance Circle</title>
<link href="https://fonts.googleapis.com/css2?family=Open+Sans:wght@300;400;600;700&display=swap" rel="stylesheet">
<style>
:root{
  --pink:#f0457a;
  --blue:#5b80c6;
  --blue-dark:#4a6fb8;
  --ink:#222;
  --text:#555;
  --muted:#888;
  --light:#f3f3f3;
  --hero:#ebebed;
  --footer:#262626;
  --white:#fff;
}
*{box-sizing:border-box;margin:0;padding:0}
html,body{width:1200px;height:3614px;overflow:hidden}
body{font-family:'Open Sans',sans-serif;color:var(--text);background:var(--white);position:relative}

/* header + hero */
.hero{position:absolute;left:0;top:0;width:1200px;height:668px;background:var(--hero);overflow:hidden}
.brand{position:absolute;left:130px;top:30px;display:flex;align-items:center;gap:12px}
.brand-dot{width:56px;height:56px;border-radius:50%;background:var(--pink);flex:none}
.brand-name{font-size:24px;font-weight:700;color:var(--pink);line-height:1.05;width:170px}
.phone{position:absolute;right:128px;top:18px;display:flex;align-items:center;gap:8px;color:var(--ink);font-size:18px;font-weight:600}
.phone small{font-size:11px;font-weight:400;color:var(--text)}
.nav{position:absolute;right:128px;top:56px;display:flex;gap:26px;align-items:center;font-size:13px;color:var(--ink)}
.nav .active{background:var(--pink);color:var(--white);padding:4px 12px}
.hero-svg{position:absolute;left:0;top:0}
.role{position:absolute;width:200px;text-align:center;font-size:15px;color:var(--ink)}
.role-icon{width:40px;height:40px;border-radius:50%;background:var(--blue);margin:0 auto 10px}
.portrait{position:absolute;left:482px;top:205px;width:236px;height:463px;border-radius:118px 118px 0 0;background:linear-gradient(180deg,#c98a6e 0%,#e0559a 45%,#e0448e 100%)}

/* mission */
.section-title{font-size:22px;font-weight:400;color:var(--ink);text-align:center}
.mission{position:absolute;top:668px;left:0;width:1200px;height:236px;border-top:1px solid #ddd}
.mission .section-title{margin-top:50px}
.mission p{width:470px;margin:22px auto 0;font-size:13.5px;line-height:1.6;text-align:center;color:var(--text)}
.quote{position:absolute;font-size:80px;color:#d8d8d8;font-family:Georgia,serif;line-height:1}

/* facts */
.facts{position:absolute;top:904px;left:0;width:1200px;height:458px;background:var(--light);border-top:1px solid #e2e2e2}
.facts .section-title{margin-top:48px;font-size:20px}
.facts .intro{width:680px;margin:22px auto 0;font-size:13px;line-height:1.6;text-align:center}
.fact{position:absolute;top:220px;width:316px;text-align:center}
.fact + .fact{border-left:1px solid #ddd}
.fact-icon{display:block;margin:0 auto}
.fact h3{font-size:15px;font-weight:600;color:var(--ink);margin-top:40px}
.fact p{width:200px;margin:14px auto 0;font-size:12px;line-height:1.45}

/* providers band */
.providers{position:absolute;top:1362px;left:0;width:1200px;height:506px;background:var(--blue);color:var(--white)}
.providers h2{margin-top:46px;font-size:20px;font-weight:300;text-align:center;line-height:1.4}
.provider{position:absolute;top:166px;width:193px;text-align:center;height:280px}
.provider + .provider{border-left:1px solid rgba(255,255,255,.35)}
.provider-icon{width:42px;height:42px;border-radius:50%;background:rgba(255,255,255,.9);margin:20px auto 0}
.provider h3{font-size:14px;font-weight:600;margin-top:32px}
.provider p{width:150px;margin:16px auto 0;font-size:11px;line-height:1.45}

/* programs */
.programs{position:absolute;top:1868px;left:0;width:1200px;height:675px}
.programs h2{margin-top:62px;font-size:20px;font-weight:400;color:var(--ink);text-align:center;line-height:1.5}
.program{position:absolute;top:164px;width:206px}
.program-photo{width:206px;height:195px;background:linear-gradient(160deg,#e9cdbd,#c79a86)}
.program h3{font-size:14px;font-weight:600;color:var(--ink);margin-top:34px}
.program p{margin-top:10px;font-size:11px;line-height:1.45;text-align:justify}

/* newsletter */
.newsletter{position:absolute;top:2543px;left:0;width:1200px;height:301px;background:linear-gradient(135deg,#6386c8,#4f75bd 60%,#6a8ccc)}
.newsletter h2{margin-top:60px;color:var(--white);font-size:22px;font-weight:600;text-align:center}
.field{position:absolute;height:37px;background:var(--white);font-size:11px;color:var(--ink);padding:11px 12px;text-transform:uppercase}
.btn{position:absolute;background:var(--pink);color:var(--white);font-size:15px;font-weight:600;text-align:center;letter-spacing:.5px}

/* join */
.join{position:absolute;top:2844px;left:0;width:1200px;height:434px;background:#f5f5f5}
.join h2{margin-top:52px;font-size:20px;font-weight:400;color:var(--ink);text-align:center}
.join .sub{text-align:center;font-size:14px;margin-top:6px;color:var(--text)}
.card{position:absolute;left:292px;top:149px;width:616px;height:217px;background:var(--white);box-shadow:0 2px 10px rgba(0,0,0,.12)}
.input{position:absolute;height:34px;border:1px solid #ccc;font-size:12px;color:var(--text);padding:8px 10px}

/* footer */
.footer{position:absolute;top:3278px;left:0;width:1200px;height:336px;background:var(--footer);color:#ddd;font-size:12px}
.footer h4{font-size:12px;font-weight:700;color:var(--white);letter-spacing:.5px;margin-bottom:18px}
.footer-brand{position:absolute;left:132px;top:70px;display:flex;align-items:center;gap:12px}
.footer-col{position:absolute;top:65px}
.contact-row{display:flex;gap:12px;align-items:flex-start;margin-bottom:18px;line-height:1.5}
.menu-list li{list-style:none;margin-bottom:6px}
.social li{list-style:none;display:flex;align-items:center;gap:12px;margin-bottom:18px}
.social-dot{width:26px;height:26px;border-radius:50%;background:var(--blue)}
.rule{position:absolute;left:132px;top:252px;width:936px;height:1px;background:#444}
.copy{position:absolute;top:292px;width:1200px;text-align:center;font-size:11px;color:#bbb}
</style>
</head>
<body>

<header class="hero">
  <svg class="hero-svg" width="1200" height="668" aria-hidden="true">
    <g stroke="#cfd0d6" stroke-width="1.5" fill="none">
      <line x1="430" y1="360" x2="400" y2="150"/>
      <line x1="770" y1="360" x2="800" y2="150"/>
      <line x1="420" y1="420" x2="240" y2="420"/>
      <line x1="780" y1="420" x2="960" y2="420"/>
    </g>
    <circle cx="600" cy="453" r="181" fill="none" stroke="#5b80c6" stroke-width="6"/>
  </svg>
  <div class="brand"><span class="brand-dot"></span><span class="brand-name">Glucose Guidance Circle</span></div>
  <div class="phone">
    <svg width="16" height="16" viewBox="0 0 24 24"><path fill="#f0457a" d="M6.6 10.8a15 15 0 0 0 6.6 6.6l2.2-2.2a1 1 0 0 1 1-.3 11 11 0 0 0 3.6.6 1 1 0 0 1 1 1V20a1 1 0 0 1-1 1A17 17 0 0 1 3 4a1 1 0 0 1 1-1h3.5a1 1 0 0 1 1 1 11 11 0 0 0 .6 3.6 1 1 0 0 1-.3 1z"/></svg>
    <small>Call Us</small> 555.010.2040
  </div>
  <nav class="nav">
    <span class="active">Home</span><span>Find a healthcare provider</span><span>Join our network</span><span>Newsletter</span><span>Blog</span>
  </nav>
  <div class="portrait" role="img" aria-label="Smiling healthcare professional in pink scrubs with arms crossed"></div>
  <div class="role" style="left:500px;top:130px"><div class="role-icon" role="img" aria-label="Educator icon"></div>Diabetic Educators</div>
  <div class="role" style="left:262px;top:268px"><div class="role-icon" role="img" aria-label="Syringe icon"></div>Endocrinologists</div>
  <div class="role" style="left:756px;top:268px"><div class="role-icon" role="img" aria-label="Carrot icon"></div>Nutritionists</div>
  <div class="role" style="left:250px;top:464px"><div class="role-icon" role="img" aria-label="Footprints icon"></div>Podiatrists</div>
  <div class="role" style="left:748px;top:464px"><div class="role-icon" role="img" aria-label="Foot icon"></div>Pedorthists</div>
</header>

<section class="mission">
  <h2 class="section-title">Our Mission</h2>
  <span class="quote" style="left:330px;top:92px">&ldquo;</span>
  <p>At the Glucose Guidance Circle, our focus is to connect newly diagnosed and existing patients with diabetes to a network of available professionals who possess the knowledge to manage your diabetes.</p>
  <span class="quote" style="left:752px;top:160px">&rdquo;</span>
</section>

<section class="facts">
  <h2 class="section-title">Diabetes Facts and Statistics</h2>
  <p class="intro">Diabetes occurs when your blood glucose, also called blood sugar, is too high. High blood glucose can cause health problems over time. The main types of diabetes are type 1, type 2, and gestational.</p>
  <div class="fact" style="left:128px">
    <svg class="fact-icon" width="56" height="50" viewBox="0 0 56 50"><g fill="#f0457a"><circle cx="28" cy="12" r="8"/><circle cx="12" cy="16" r="6"/><circle cx="44" cy="16" r="6"/><path d="M14 48c0-14 6-22 14-22s14 8 14 22z"/><path d="M0 46c0-10 4-16 11-16 3 0 5 1 6 3-3 4-4 8-4 13z"/><path d="M56 46c0-10-4-16-11-16-3 0-5 1-6 3 3 4 4 8 4 13z"/></g></svg>
    <h3>Total</h3>
    <p>An estimated 30.3 million people have diabetes (9.4 percent of the U.S. population)</p>
  </div>
  <div class="fact" style="left:444px">
    <svg class="fact-icon" width="56" height="52" viewBox="0 0 56 52"><path fill="#f0457a" d="M28 50 6 28A14 14 0 0 1 28 10a14 14 0 0 1 22 18z"/><path d="M10 28h12l4-8 5 14 4-6h11" stroke="#fff" stroke-width="3" fill="none"/></svg>
    <h3>Diagnosed</h3>
    <p>An estimated 23.1 million people have been diagnosed with diabetes (7.2 percent of the U.S. population)</p>
  </div>
  <div class="fact" style="left:760px">
    <svg class="fact-icon" width="52" height="54" viewBox="0 0 52 54"><g fill="none" stroke="#f0457a" stroke-width="4"><path d="M8 4v14a12 12 0 0 0 24 0V4"/><path d="M20 30v8a10 10 0 0 0 20 0v-6"/><circle cx="40" cy="26" r="5"/></g></svg>
    <h3>Undiagnosed</h3>
    <p>An estimated 7.2 million adults, ages 18 years or older are undiagnosed (23.8 percent of people with diabetes)</p>
  </div>
</section>

<section class="providers">
  <h2>Our network of healthcare providers will<br>help you manage your diabetes</h2>
  <div class="provider" style="left:120px"><div class="provider-icon" role="img" aria-label="Foot icon"></div><h3>Pedorthist</h3><p>A professional who has specialized training in foot evaluation and modification of footwear and supportive devices such as inserts, to address conditions which affect the feet and lower limbs caused by disease, defect or injury.</p></div>
  <div class="provider" style="left:313px"><div class="provider-icon" role="img" aria-label="Educator icon"></div><h3>Diabetic Educator</h3><p>A health professional who possesses knowledge of and experience in diabetes prevention, pre-diabetes, and diabetes management. Their main goal is to achieve individualized behavioral and treatment goals that reduce risks and optimize healthy lifestyles.</p></div>
  <div class="provider" style="left:506px"><div class="provider-icon" role="img" aria-label="Syringe icon"></div><h3>Endocrinologist</h3><p>A physician who specializes in treating disorders of the endocrine system, such as diabetes.</p></div>
  <div class="provider" style="left:699px"><div class="provider-icon" role="img" aria-label="Carrot icon"></div><h3>Nutritionists</h3><p>An expert in dietetics; which includes human nutrition and the regulation of diet. A dietitian alters their patient's nutrition based upon their medical condition and individual needs.</p></div>
  <div class="provider" style="left:892px"><div class="provider-icon" role="img" aria-label="Footprints icon"></div><h3>Podiatrist</h3><p>A doctor qualified and trained to diagnose and treat conditions affecting the foot, ankle, and related structures of the leg.</p></div>
</section>

<section class="programs">
  <h2>Did you know that the government has setup programs to<br>help educate, manage, and prevent your diabetes?</h2>
  <article class="program" style="left:133px">
    <div class="program-photo" role="img" aria-label="Hands examining a bare foot"></div>
    <h3>Pedorthist Services</h3>
    <p>Diabetic Shoes - the furnishing and fitting of either one pair of custom-molded shoes and inserts or one pair of extra-depth shoes each calendar year. CareCover also covers 2 additional pairs of inserts each calendar year for custom-molded shoes and 3 pairs of inserts each calendar year for extra-depth shoes. CareCover will cover shoe modifications instead of inserts.</p>
  </article>
  <article class="program" style="left:373px">
    <div class="program-photo" role="img" aria-label="Nutritionist with fresh fruit and vegetables" style="background:linear-gradient(160deg,#dfe8f2,#7fa6d3 60%,#e2a05a)"></div>
    <h3>Nutritionists</h3>
    <p>Medical Nutrition Therapy - often abbreviated as MNT, is an evidence-based medical approach to treating certain chronic conditions through the use of an individually-tailored nutrition plan. This nutrition plan is ordered and approved by a primary care physician and implemented by a Registered Nutritionist.</p>
  </article>
  <article class="program" style="left:617px">
    <div class="program-photo" role="img" aria-label="Educator reviewing a clipboard with an older patient" style="background:linear-gradient(160deg,#eef0f2,#b9c3cf)"></div>
    <h3>Diabetic Educators</h3>
    <p>Diabetes self-management training (DSMT) - The purpose of CareCover's DSMT benefit is to give beneficiaries the knowledge and skills needed to adopt diabetes self-care behaviors and to make lifestyle changes needed to improve health outcomes. Beneficiaries are covered for a total of 10 hours of initial training within a continuous 12-month period and 2 hours of follow-up training each year after that, as needed. Courses are offered</p>
  </article>
  <article class="program" style="left:860px">
    <div class="program-photo" role="img" aria-label="Close view of bare feet on a soft floor" style="background:linear-gradient(160deg,#f0e6e2,#d7aa98)"></div>
    <h3>Podiatrist</h3>
    <p>Foot exams - podiatrist services such as foot exams every 6 months, foot injuries or diseases (like hammer toes, bunion deformities, and heel spurs).</p>
  </article>
</section>

<section class="newsletter" role="img" aria-label="Blue tinted photo of a foot examination behind the signup form">
  <h2>Sign up for Our Newsletter</h2>
  <div class="field" style="left:280px;top:122px;width:204px">First Name</div>
  <div class="field" style="left:499px;top:122px;width:205px">Last Name</div>
  <div class="field" style="left:718px;top:122px;width:205px">E Mail</div>
  <div class="btn" style="left:535px;top:202px;width:128px;height:43px;line-height:39px;border:2px solid #fff">SIGN UP</div>
</section>

<section class="join">
  <h2>Healthcare Professional</h2>
  <p class="sub">Sign up to be part of our network</p>
  <div class="card">
    <div class="input" style="left:24px;top:29px;width:276px">First Name</div>
    <div class="input" style="left:316px;top:29px;width:276px">Last Name</div>
    <div class="input" style="left:24px;top:77px;width:180px">Phone</div>
    <div class="input" style="left:216px;top:77px;width:180px">Email</div>
    <div class="input" style="left:408px;top:77px;width:184px">Profession
      <svg style="position:absolute;right:12px;top:14px" width="8" height="5"><path d="M0 0h8L4 5z" fill="#555"/></svg>
    </div>
    <div class="btn" style="left:255px;top:150px;width:106px;height:34px;line-height:34px;font-size:14px">SUBMIT</div>
  </div>
</section>

<footer class="footer">
  <div class="footer-brand"><span class="brand-dot" style="width:72px;height:72px"></span><span class="brand-name" style="font-size:26px;width:190px">Glucose Guidance Circle</span></div>
  <div class="footer-col" style="left:429px">
    <h4>CONTACT US</h4>
    <div class="contact-row"><svg width="10" height="14" viewBox="0 0 10 14"><path fill="#fff" d="M5 0a5 5 0 0 1 5 5c0 4-5 9-5 9S0 9 0 5a5 5 0 0 1 5-5zm0 3a2 2 0 1 0 0 4 2 2 0 0 0 0-4z"/></svg><span>118 Maple Court<br>Brookfield, IL 60400</span></div>
    <div class="contact-row"><svg width="12" height="12" viewBox="0 0 24 24"><path fill="#fff" d="M6.6 10.8a15 15 0 0 0 6.6 6.6l2.2-2.2a1 1 0 0 1 1-.3 11 11 0 0 0 3.6.6 1 1 0 0 1 1 1V20a1 1 0 0 1-1 1A17 17 0 0 1 3 4a1 1 0 0 1 1-1h3.5a1 1 0 0 1 1 1 11 11 0 0 0 .6 3.6 1 1 0 0 1-.3 1z"/></svg><span>555.010.2040</span></div>
    <div class="contact-row"><svg width="13" height="10" viewBox="0 0 13 10"><rect width="13" height="10" fill="#fff"/><path d="M0 0l6.5 5L13 0" stroke="#262626" fill="none"/></svg><span>hello@glucoseguidancecircle.example</span></div>
  </div>
  <div class="footer-col" style="left:694px">
    <h4>MENU</h4>
    <ul class="menu-list"><li>Home</li><li>Find a healthcare provider</li><li>Join our network</li><li>Newsletter</li><li>Blog</li></ul>
  </div>
  <div class="footer-col" style="left:966px">
    <h4>FOLLOW US ON</h4>
    <ul class="social"><li><span class="social-dot"></span>Circlebook</li><li><span class="social-dot"></span>Chirpline</li><li><span class="social-dot"></span>ProLinker</li></ul>
  </div>
  <div class="rule"></div>
  <p class="copy">Copyrights @ 2018 All Rights Reserved</p>
</footer>

</body>
</html>
```